Powerpoint template for Presenting Java Related Training

I am launching a website in 2017 called Quill Harbor Labs that will offer training on advanced topics in Java programming. I need a Powerpoint template for use in the training courses. I have attached my logo. I am also attaching my business card design which was just completed ... I'd like to stay somewhat consistent between the different media, but without making the Powerpoint template too busy.
Updates

Project Deadline Extended Reason: Only 3 designs received and 2 days left so I am extending the deadline by 5 days. I would like to have at least 5 or 6 designs to consider before I make my decision. Added Sunday, October 30, 2016

Target Market(s)

Current and Prospective Software Developers

Industry/Entity Type

Software

Font styles to use
Serif
Sans Serif

Requirements
Must have
• Must use the provided logo and must use a color scheme that works well with the logo provided. Must be easy to read since this is for a training presentation and I don't want any distractions from the content.
Nice to have
• I would like to have alternatives for different types of content ... e.g. bullet lists vs. graphics, etc.
Should not have
• Just not too busy ... I want something that looks distinctive and nice but with minimal distractions.

```html
<!DOCTYPE html>
<html lang="en">
<head>
<meta charset="utf-8">
<title>Quill Harbor Labs – Presentation Template</title>
<link href="https://fonts.googleapis.com/css2?family=Open+Sans:wght@300;400;600;700&display=swap" rel="stylesheet">
<style>
:root{
  --red:#e8353b;--red-d:#c4252b;--blue:#1c5fae;--blue-d:#154a8a;
  --ink:#333;--mute:#8a8a8a;--line:#e3e3e3;--soft:#f3f3f3;--white:#fff;
}
*{box-sizing:border-box;margin:0;padding:0}
html,body{width:1200px;height:3545px;overflow:hidden;background:#e9e9e9}
body{font-family:'Open Sans',Arial,sans-serif;color:var(--ink)}
.deck{width:1200px;height:3545px;padding:4px;display:grid;grid-template-columns:repeat(3,1fr);grid-template-rows:repeat(16,1fr);gap:6px}
.slide{position:relative;background:var(--white);overflow:hidden}
.abs{position:absolute}
.ft{position:absolute;left:0;right:0;bottom:0;height:9px;background:var(--red);color:#fff;font-size:4px;line-height:9px;padding-left:8px}
.ft::after{content:"";position:absolute;right:8px;top:0;width:12px;height:9px;background:var(--blue)}
.brand{position:absolute;top:7px;right:8px;font-size:6px;font-weight:700;color:var(--red);display:flex;align-items:center;gap:2px;letter-spacing:.2px;white-space:nowrap}
.brand i{width:7px;height:7px;border-radius:50%;background:var(--red)}
.brand.w{color:#fff}.brand.w i{background:#fff}
.ttl{position:absolute;top:12px;left:12px;font-size:13px;font-weight:400;color:var(--ink);white-space:nowrap}
.ttl b{font-weight:400;border-bottom:1.5px solid var(--red)}
.ph{position:absolute;background:linear-gradient(135deg,#cfc8c0,#7b736d)}
.ph.blue{background:linear-gradient(135deg,#58a6dc,#0f3f7a)}
.ph.red{background:linear-gradient(135deg,#e0474c,#9b1c22)}
.ph.dark{background:linear-gradient(135deg,#5a5e66,#1d2025)}
.ph.light{background:linear-gradient(135deg,#ebe7e2,#b7b0a8)}
.ph.warm{background:linear-gradient(135deg,#d9b99a,#7a5b45)}
.p{font-size:4.4px;line-height:1.55;color:#7a7a7a}
.p.w{color:#fde}
.h{font-size:6px;font-weight:700;color:var(--ink);margin-bottom:1px}
.h.w{color:#fff}
.h.r{color:var(--red)}
.lead{font-size:7px;font-weight:600;color:var(--ink);line-height:1.3}
.lead em{font-style:normal;color:var(--red)}
.ic{flex:none;width:12px;height:12px;border-radius:50%;background:var(--red);position:relative}
.ic.b{background:var(--blue)}.ic.wh{background:#fff}
.ic::after{content:"";position:absolute;left:4.5px;top:2.5px;width:3px;height:5px;border:solid #fff;border-width:0 1.2px 1.2px 0;transform:rotate(45deg)}
.ic.wh::after{border-color:var(--red)}
.it{display:flex;gap:5px;align-items:flex-start}
.col{display:flex;flex-direction:column}
.red-bg{background:var(--red)}.blue-bg{background:var(--blue)}
.c{text-align:center}
.num{flex:none;width:14px;height:14px;background:var(--red);color:#fff;font-size:7px;font-weight:700;display:flex;align-items:center;justify-content:center}
.num.b{background:var(--blue)}
.big-ttl{font-size:15px;font-weight:300;color:#fff}
.circ{border-radius:50%;display:flex;align-items:center;justify-content:center;color:#fff;font-weight:700}
</style>
</head>
<body>
<main class="deck">

<section class="slide red-bg">
  <div class="abs c" style="left:0;right:0;top:62px">
    <div style="width:26px;height:26px;border-radius:50%;background:#fff;margin:0 auto 8px"></div>
    <div style="font-size:22px;font-weight:700;color:#fff;letter-spacing:1px">QUILL HARBOR LABS</div>
    <div style="font-size:6px;color:#fff;margin-top:3px">Be an Expert with Us</div>
  </div>
</section>

<section class="slide">
  <div class="ph warm" role="img" aria-label="Photo of developers smiling in an office" style="left:0;top:0;width:100%;height:120px"></div>
  <div class="brand" style="top:90px;right:auto;left:150px;background:#fff;padding:3px 5px"><i></i>QUILL HARBOR LABS</div>
  <div class="abs red-bg c" style="left:0;right:0;top:120px;height:34px;padding-top:6px">
    <div class="big-ttl">Your Title Goes Here</div>
    <div style="font-size:4.5px;color:#fff">Your subtitle goes here</div>
  </div>
  <div class="abs" style="left:40px;right:40px;top:166px;display:flex;justify-content:space-between">
    <div class="it"><span class="ic" style="width:8px;height:8px"></span><div class="p">Presenter Name<br>Senior Trainer</div></div>
    <div class="it"><span class="ic" style="width:8px;height:8px"></span><div class="p">Course Date<br>Session One</div></div>
    <div class="it"><span class="ic" style="width:8px;height:8px"></span><div class="p">Lab Room<br>Main Campus</div></div>
  </div>
  <div class="ft">Quill Harbor Labs</div>
</section>

<section class="slide">
  <div class="ph dark" role="img" aria-label="Photo of a young man in a dark studio" style="left:0;top:0;width:100%;height:120px"></div>
  <svg class="abs" style="left:0;top:0" width="393" height="120"><polygon points="0,0 160,0 110,120 0,120" fill="#111" opacity=".55"/></svg>
  <div class="brand w" style="top:40px;left:20px;right:auto;font-size:8px"><i></i>QUILL HARBOR LABS</div>
  <div class="abs red-bg c" style="left:0;right:0;top:120px;height:34px;padding-top:6px">
    <div class="big-ttl">Your Title Goes Here</div>
    <div style="font-size:4.5px;color:#fff">Your subtitle goes here</div>
  </div>
  <div class="abs" style="left:40px;right:40px;top:166px;display:flex;justify-content:space-between">
    <div class="it"><span class="ic b" style="width:8px;height:8px"></span><div class="p">Presenter Name<br>Senior Trainer</div></div>
    <div class="it"><span class="ic b" style="width:8px;height:8px"></span><div class="p">Course Date<br>Session Two</div></div>
    <div class="it"><span class="ic b" style="width:8px;height:8px"></span><div class="p">Lab Room<br>Main Campus</div></div>
  </div>
  <div class="ft">Quill Harbor Labs</div>
</section>

<section class="slide">
  <div class="ttl"><b>Our</b> Agenda</div><div class="brand"><i></i>QUILL HARBOR LABS</div>
  <div class="abs" style="left:40px;top:52px;display:grid;grid-template-columns:150px 150px;gap:22px 40px">
    <div class="it"><span class="num">1</span><div><div class="h">Agenda One</div><div class="p">Short note about this topic.</div></div></div>
    <div class="it"><span class="num">4</span><div><div class="h">Agenda Four</div><div class="p">Short note about this topic.</div></div></div>
    <div class="it"><span class="num">2</span><div><div class="h">Agenda Two</div><div class="p">Short note about this topic.</div></div></div>
    <div class="it"><span class="num">5</span><div><div class="h">Agenda Five</div><div class="p">Short note about this topic.</div></div></div>
    <div class="it"><span class="num">3</span><div><div class="h">Agenda Three</div><div class="p">Short note about this topic.</div></div></div>
    <div class="it"><span class="num">6</span><div><div class="h">Agenda Six</div><div class="p">Short note about this topic.</div></div></div>
  </div>
  <div class="ft">Quill Harbor Labs</div>
</section>

<section class="slide">
  <div class="ttl"><b>Our</b> Vision &amp; Mission</div><div class="brand"><i></i>QUILL HARBOR LABS</div>
  <div class="abs red-bg" style="left:0;right:0;top:38px;height:130px"></div>
  <div class="abs" style="left:16px;top:50px;width:170px">
    <div style="font-size:9px;color:#fff;font-weight:600;line-height:1.25">Our Vision:<br>Become the leading source of advanced coding skills</div>
    <div class="p w" style="margin-top:6px">We help developers grow through deep, hands-on courses built around real projects.</div>
  </div>
  <div class="abs" style="left:206px;top:50px;width:170px">
    <div style="font-size:9px;color:#fff;font-weight:600">Our Mission:</div>
    <div class="col" style="gap:7px;margin-top:6px">
      <div class="it"><span class="ic wh"></span><div><div class="h w">First Item Here</div><div class="p w">A short line of detail.</div></div></div>
      <div class="it"><span class="ic wh"></span><div><div class="h w">Second Item Here</div><div class="p w">A short line of detail.</div></div></div>
      <div class="it"><span class="ic wh"></span><div><div class="h w">Third Item Here</div><div class="p w">A short line of detail.</div></div></div>
    </div>
  </div>
  <div class="ft">Quill Harbor Labs</div>
</section>

<section class="slide">
  <div class="ttl"><b>Our</b> Services</div><div class="brand"><i></i>QUILL HARBOR LABS</div>
  <div class="ph" role="img" aria-label="Photo of a team meeting around a laptop" style="left:12px;top:40px;width:110px;height:80px"></div>
  <div class="ph warm" role="img" aria-label="Photo of a developer at a desk" style="left:126px;top:40px;width:70px;height:80px"></div>
  <div class="abs" style="left:12px;top:128px;width:180px"><div class="h">Your Text Here</div><div class="p">Describe the service in a short paragraph that explains the value for learners.</div></div>
  <div class="abs col" style="left:220px;top:45px;gap:14px;width:160px">
    <div class="it"><span class="ic b"></span><div><div class="h">Service Number One</div><div class="p">A short line about this service.</div></div></div>
    <div class="it"><span class="ic b"></span><div><div class="h">Service Number Two</div><div class="p">A short line about this service.</div></div></div>
    <div class="it"><span class="ic b"></span><div><div class="h">Service Number Three</div><div class="p">A short line about this service.</div></div></div>
  </div>
  <div class="ft">Quill Harbor Labs</div>
</section>

<section class="slide">
  <div class="ph warm" role="img" aria-label="Photo of smiling students in a classroom" style="left:0;top:0;width:100%;height:206px"></div>
  <div class="abs red-bg" style="left:196px;top:30px;width:180px;height:120px;padding:14px 14px">
    <div style="font-size:13px;color:#fff;margin-bottom:6px">About Us</div>
    <div class="p w">We are a small team of engineers who teach the advanced topics most courses skip.</div>
    <div class="p w" style="margin-top:5px">Every lesson is practical, focused and built to help you ship better code.</div>
  </div>
  <div class="ft">Quill Harbor Labs</div>
</section>

<section class="slide">
  <div class="ttl"><b>Your</b> Title</div><div class="brand"><i></i>QUILL HARBOR LABS</div>
  <div class="abs" style="left:12px;top:48px;width:100px"><div class="h">Heading Goes Here</div><div class="p">Add a short paragraph that supports your main message on this slide.</div><div class="p" style="margin-top:5px">Keep it brief and easy to scan.</div></div>
  <div class="ph dark" role="img" aria-label="Photo of a businessman with a digital interface" style="left:120px;top:36px;width:140px;height:160px"></div>
  <div class="abs col" style="left:272px;top:48px;gap:10px;width:112px">
    <div class="it"><span class="ic"></span><div><div class="h">Your Text Here</div><div class="p">Short detail line.</div></div></div>
    <div class="it"><span class="ic"></span><div><div class="h">Your Text Here</div><div class="p">Short detail line.</div></div></div>
    <div class="it"><span class="ic"></span><div><div class="h">Your Text Here</div><div class="p">Short detail line.</div></div></div>
    <div class="it"><span class="ic"></span><div><div class="h">Your Text Here</div><div class="p">Short detail line.</div></div></div>
  </div>
  <div class="ft">Quill Harbor Labs</div>
</section>

<section class="slide">
  <div class="ph warm" role="img" aria-label="Photo of two colleagues looking at a screen" style="left:0;top:0;width:200px;height:206px"></div>
  <div class="abs red-bg c" style="left:40px;top:130px;width:110px;height:50px;padding-top:19px;font-size:8px;font-weight:700;color:#fff;white-space:nowrap">QUILL HARBOR LABS</div>
  <div class="brand"><i></i>QUILL HARBOR LABS</div>
  <div class="abs" style="left:214px;top:44px;font-size:14px;line-height:1.2">Your Title Goes Here</div>
  <div class="abs col" style="left:214px;top:96px;gap:12px;width:165px">
    <div class="it"><span class="ic b"></span><div><div class="h">First Text Here</div><div class="p">Add a short note to support this point.</div></div></div>
    <div class="it"><span class="ic b"></span><div><div class="h">Your Text Here</div><div class="p">Add a short note to support this point.</div></div></div>
  </div>
  <div class="ft">Quill Harbor Labs</div>
</section>

<section class="slide">
  <div class="ph blue" role="img" aria-label="Photo of a hand touching a glowing screen" style="left:0;top:0;width:100%;height:206px"></div>
  <div class="abs red-bg" style="left:190px;top:0;width:203px;height:206px;padding:22px 16px">
    <div class="h w" style="font-size:7px">We are Quill Harbor Labs</div>
    <div class="p w" style="margin-bottom:10px">Be an expert with us</div>
    <div class="col" style="gap:10px">
      <div class="it"><span class="ic wh"></span><div><div class="h w">Your Text Here</div><div class="p w">A short line of supporting text.</div></div></div>
      <div class="it"><span class="ic wh"></span><div><div class="h w">Your Text Here</div><div class="p w">A short line of supporting text.</div></div></div>
      <div class="it"><span class="ic wh"></span><div><div class="h w">Your Text Here</div><div class="p w">A short line of supporting text.</div></div></div>
    </div>
  </div>
  <div class="ft">Quill Harbor Labs</div>
</section>

<section class="slide red-bg">
  <div class="abs circ" style="left:184px;top:48px;width:22px;height:22px;background:#fff;color:var(--red);font-size:14px">“</div>
  <div class="abs c" style="left:60px;right:60px;top:86px;font-size:9px;color:#fff;line-height:1.45;font-weight:300">Coming together is a beginning. Keeping together is progress. Working together is success.</div>
  <div class="abs c" style="left:0;right:0;top:136px;font-size:4.5px;color:#fff">Author Name</div>
  <div class="ft">Quill Harbor Labs</div>
</section>

<section class="slide">
  <div class="ttl"><b>Quote</b> Area</div><div class="brand"><i></i>QUILL HARBOR LABS</div>
  <div class="ph blue" role="img" aria-label="Blue photo of a modern office" style="left:0;top:40px;width:100%;height:150px"></div>
  <div class="abs red-bg" style="left:12px;top:56px;width:170px;height:90px;padding:14px">
    <div style="font-size:7px;color:#fff;line-height:1.45">“ Coming together is a beginning. Keeping together is progress. Working together is success.</div>
    <div class="p w" style="margin-top:6px">Author Name</div>
  </div>
  <div class="ft">Quill Harbor Labs</div>
</section>

<section class="slide">
  <div class="ttl"><b>Your</b> Title Goes Here</div><div class="brand"><i></i>QUILL HARBOR LABS</div>
  <div class="abs" style="left:12px;top:44px;width:110px">
    <div class="lead">We are <em>Quill Harbor Labs</em><br>Be an Expert with Us</div>
    <div class="p" style="margin-top:6px">Describe what learners get from this module in a few short lines.</div>
    <div class="p" style="margin-top:5px">Add a second point that adds more context for the group.</div>
  </div>
  <div class="ph" role="img" aria-label="Photo of a student with a laptop" style="left:140px;top:40px;width:115px;height:74px"></div>
  <div class="ph warm" role="img" aria-label="Photo of a man smiling at work" style="left:260px;top:40px;width:120px;height:74px"></div>
  <div class="ph warm" role="img" aria-label="Photo of a developer typing" style="left:140px;top:118px;width:115px;height:74px"></div>
  <div class="ph" role="img" aria-label="Photo of colleagues talking" style="left:260px;top:118px;width:120px;height:74px"></div>
  <div class="ft">Quill Harbor Labs</div>
</section>

<section class="slide">
  <div class="ttl"><b>Our</b> Differences</div><div class="brand"><i></i>QUILL HARBOR LABS</div>
  <div class="abs col" style="left:30px;top:52px;gap:10px;width:190px">
    <div class="it"><span class="ic b"></span><div class="p">Short line that explains what makes this course different.</div></div>
    <div class="it"><span class="ic b"></span><div class="p">Short line that explains what makes this course different.</div></div>
    <div class="it"><span class="ic b"></span><div class="p">Short line that explains what makes this course different.</div></div>
    <div class="it"><span class="ic b"></span><div class="p">Short line that explains what makes this course different.</div></div>
  </div>
  <div class="ph warm" role="img" aria-label="Photo of two people at a laptop" style="left:230px;top:56px;width:110px;height:80px"></div>
  <div class="ft">Quill Harbor Labs</div>
</section>

<section class="slide">
  <div class="ttl"><b>Your</b> Title Goes Here</div><div class="brand"><i></i>QUILL HARBOR LABS</div>
  <div class="abs" style="left:12px;top:38px;width:170px"><div class="h">Heading Goes Here</div><div class="p">A short intro line for the list below.</div></div>
  <div class="abs col" style="left:12px;top:70px;gap:12px;width:160px">
    <div class="it"><span class="ic"></span><div><div class="h">Sample Number One</div><div class="p">Add a brief detail.</div></div></div>
    <div class="it"><span class="ic"></span><div><div class="h">Sample Number Two</div><div class="p">Add a brief detail.</div></div></div>
    <div class="it"><span class="ic"></span><div><div class="h">Sample Number Three</div><div class="p">Add a brief detail.</div></div></div>
  </div>
  <div class="abs col" style="left:196px;top:44px;width:186px;gap:6px">
    <div style="display:flex;height:36px"><span class="num" style="width:26px;height:36px;font-size:12px">1</span><div class="red-bg p w" style="flex:1;padding:6px">Write a short description for this step here.</div></div>
    <div style="display:flex;height:36px"><span class="num b" style="width:26px;height:36px;font-size:12px">2</span><div class="blue-bg p w" style="flex:1;padding:6px">Write a short description for this step here.</div></div>
    <div style="display:flex;height:36px"><span class="num" style="width:26px;height:36px;font-size:12px">3</span><div class="red-bg p w" style="flex:1;padding:6px">Write a short description for this step here.</div></div>
  </div>
  <div class="ft">Quill Harbor Labs</div>
</section>

<section class="slide">
  <div class="ttl"><b>Text</b> Area</div><div class="brand"><i></i>QUILL HARBOR LABS</div>
  <div class="abs" style="left:12px;top:44px;width:360px">
    <div class="lead">We are <em>Quill Harbor Labs</em><br>Be an Expert with Us</div>
    <div class="p" style="margin-top:8px">Use this space for a longer block of text that explains the core idea of the lesson. Keep sentences short and clear so the group can follow along while you speak.</div>
    <div class="p" style="margin-top:6px">Add a second paragraph that gives an example, a quick tip or a link to the next section of the course.</div>
    <div class="p" style="margin-top:6px">Close with a short summary that learners can take away.</div>
  </div>
  <div class="ft">Quill Harbor Labs</div>
</section>

<section class="slide">
  <div class="ph red" role="img" aria-label="Red toned photo of a hand with glowing network lines" style="left:0;top:0;width:100%;height:206px"></div>
  <div class="abs c" style="left:0;right:0;top:86px"><div class="big-ttl">Your Title Goes Here</div><div style="font-size:5px;color:#fff">Your subtitle here</div></div>
  <div class="ft">Quill Harbor Labs</div>
</section>

<section class="slide">
  <div class="abs" style="left:260px;top:0;width:133px;height:206px;background:var(--blue)"></div>
  <div class="abs" style="left:12px;top:16px;width:340px;height:174px;background:#fff;border-top:3px solid var(--red);box-shadow:0 0 6px rgba(0,0,0,.15);padding:12px">
    <div style="font-size:13px">Text Area</div>
    <div class="lead" style="margin-top:6px">We are <em>Quill Harbor Labs</em><br>Be an Expert with Us</div>
    <div class="p" style="margin-top:6px">Use this space for a longer block of text that explains the core idea of the lesson in clear, simple words.</div>
    <div class="p" style="margin-top:5px">Add a second paragraph with an example or a quick tip for the group.</div>
  </div>
  <div class="brand"><i></i>QUILL HARBOR LABS</div>
  <div class="ft">Quill Harbor Labs</div>
</section>

<section class="slide">
  <div class="abs red-bg" style="left:0;top:0;width:110px;height:206px"></div>
  <div class="abs c" style="left:0;top:28px;width:110px;font-size:8px;font-weight:700;color:#fff;white-space:nowrap">QUILL HARBOR LABS</div>
  <div class="ph light" role="img" aria-label="Photo of a man working on a laptop" style="left:60px;top:70px;width:180px;height:120px"></div>
  <div class="brand"><i></i>QUILL HARBOR LABS</div>
  <div class="abs" style="left:256px;top:40px;font-size:13px;line-height:1.2">Your Title<br>Goes Here</div>
  <div class="abs" style="left:256px;top:84px;width:125px"><div class="p">Add a short paragraph describing this part of the course.</div></div>
  <div class="ft">Quill Harbor Labs</div>
</section>

<section class="slide">
  <div class="ttl"><b>Your</b> Title Goes Here</div><div class="brand"><i></i>QUILL HARBOR LABS</div>
  <div class="ph" role="img" aria-label="Photo of a team working together" style="left:12px;top:44px;width:120px;height:80px"></div>
  <div class="ph warm" role="img" aria-label="Photo of people in a meeting" style="left:136px;top:44px;width:120px;height:80px"></div>
  <div class="ph" role="img" aria-label="Photo of a workshop session" style="left:260px;top:44px;width:120px;height:80px"></div>
  <div class="abs blue-bg" style="left:150px;top:56px;width:100px;height:56px;padding:6px"><div class="h w">Heading Goes Here</div><div class="p w">Short detail line for this card.</div></div>
  <div class="abs red-bg" style="left:12px;top:124px;width:120px;height:46px;padding:6px"><div class="h w">THIS IS YOUR TEXT</div><div class="p w">Short detail for this card.</div></div>
  <div class="abs red-bg" style="left:260px;top:124px;width:120px;height:46px;padding:6px"><div class="h w">THIS IS YOUR TEXT</div><div class="p w">Short detail for this card.</div></div>
  <div class="ft">Quill Harbor Labs</div>
</section>

<section class="slide">
  <div class="ttl"><b>Portfolio</b> Area</div><div class="brand"><i></i>QUILL HARBOR LABS</div>
  <div class="abs" style="left:12px;top:38px;width:170px"><div class="p">A short intro for the portfolio list.</div></div>
  <div class="abs col" style="left:12px;top:60px;gap:10px;width:160px">
    <div class="it"><span class="ic"></span><div><div class="h">First Text Here</div><div class="p">Brief detail.</div></div></div>
    <div class="it"><span class="ic b"></span><div><div class="h">Your Text Here</div><div class="p">Brief detail.</div></div></div>
    <div class="it"><span class="ic"></span><div><div class="h">Your Text Three</div><div class="p">Brief detail.</div></div></div>
    <div class="it"><span class="ic b"></span><div><div class="h">Your Text Four</div><div class="p">Brief detail.</div></div></div>
  </div>
  <div class="ph dark" role="img" aria-label="Photo of a modern office interior" style="left:196px;top:20px;width:90px;height:176px"></div>
  <div class="ph" role="img" aria-label="Photo of an open workspace" style="left:290px;top:20px;width:95px;height:176px"></div>
  <div class="ft">Quill Harbor Labs</div>
</section>

<section class="slide">
  <div class="ttl"><b>Two</b> Column Description</div><div class="brand"><i></i>QUILL HARBOR LABS</div>
  <div class="abs" style="left:12px;top:44px;width:170px">
    <div class="lead">We are <em>Quill Harbor Labs</em><br>Be an Expert with Us</div>
    <div class="p" style="margin-top:6px">Use this column for the first part of the description. Keep each line simple.</div>
    <div class="p" style="margin-top:5px">Add a second paragraph with an example for the group.</div>
  </div>
  <div class="abs" style="left:206px;top:44px;width:170px">
    <div class="p">Use this column for the second part of the description and close the idea clearly.</div>
    <div class="p" style="margin-top:5px">Add a quick tip or a reminder for the next lab.</div>
    <div class="p" style="margin-top:5px">Finish with a short takeaway for learners.</div>
  </div>
  <div class="ft">Quill Harbor Labs</div>
</section>

<section class="slide">
  <div class="ph warm" role="img" aria-label="Photo of a man working at a laptop in an office" style="left:0;top:0;width:100%;height:206px"></div>
  <div class="abs red-bg" style="left:210px;top:0;width:183px;height:206px;padding:24px 16px">
    <div style="font-size:10px;font-weight:700;color:#fff;white-space:nowrap">QUILL HARBOR LABS</div>
    <div class="abs blue-bg" style="left:0;top:110px;width:183px;height:50px;padding:8px 16px"><div style="font-size:9px;color:#fff">Your Title Goes Here</div><div class="p w">Short subtitle line here.</div></div>
  </div>
  <div class="ft">Quill Harbor Labs</div>
</section>

<section class="slide">
  <div class="ttl"><b>Three</b> Column Description</div><div class="brand"><i></i>QUILL HARBOR LABS</div>
  <div class="abs" style="left:12px;top:44px;width:115px">
    <div class="lead">We are <em>Quill Harbor Labs</em><br>Be an Expert with Us</div>
    <div class="p" style="margin-top:6px">First column text with a short idea for the group.</div>
    <div class="p" style="margin-top:5px">Add a second short paragraph.</div>
  </div>
  <div class="abs" style="left:139px;top:44px;width:115px"><div class="p">Second column text that continues the idea in simple words.</div><div class="p" style="margin-top:5px">Add one more helpful line.</div></div>
  <div class="abs" style="left:266px;top:44px;width:115px"><div class="p">Third column text that wraps up the topic for learners.</div><div class="p" style="margin-top:5px">Close with a takeaway.</div></div>
  <div class="ft">Quill Harbor Labs</div>
</section>

<section class="slide">
  <div class="ph light" role="img" aria-label="Photo of a man at a desk with a laptop" style="left:120px;top:0;width:273px;height:206px"></div>
  <div class="abs" style="left:12px;top:40px;font-size:13px;line-height:1.2">Your Title<br>Goes Here</div>
  <div class="abs" style="left:12px;top:82px;width:100px"><div class="p">Add a short paragraph that frames this section.</div><div class="p" style="margin-top:5px">Keep it clear and brief.</div></div>
  <div class="brand"><i></i>QUILL HARBOR LABS</div>
  <div class="ft">Quill Harbor Labs</div>
</section>

<section class="slide red-bg">
  <div class="abs" style="left:150px;top:70px;width:14px;height:14px;border:1.5px solid #fff;border-radius:0 0 5px 5px"></div>
  <div class="abs" style="left:135px;top:94px;font-size:11px;color:#fff;font-weight:600;letter-spacing:.5px">COFFEE BREAK</div>
  <div class="abs" style="left:135px;top:110px;font-size:4.5px;color:#fff">Back in fifteen minutes</div>
  <div class="ft">Quill Harbor Labs</div>
</section>

<section class="slide">
  <div class="ttl"><b>Your</b> Title Goes Here</div><div class="brand"><i></i>QUILL HARBOR LABS</div>
  <div class="abs col" style="left:12px;top:48px;gap:14px;width:180px">
    <div class="it"><span class="ic"></span><div><div class="h">Heading Text</div><div class="p">A short line of supporting detail.</div></div></div>
    <div class="it"><span class="ic b"></span><div><div class="h">Heading Text</div><div class="p">A short line of supporting detail.</div></div></div>
    <div class="it"><span class="ic"></span><div><div class="h">Heading Three</div><div class="p">A short line of supporting detail.</div></div></div>
  </div>
  <div class="ph warm" role="img" aria-label="Photo of a team around a table" style="left:220px;top:100px;width:160px;height:96px"></div>
  <div class="ft">Quill Harbor Labs</div>
</section>

<section class="slide">
  <div class="ttl"><b>Four</b> Bullets with Paragraph</div><div class="brand"><i></i>QUILL HARBOR LABS</div>
  <div class="abs" style="left:12px;top:54px;display:grid;grid-template-columns:100px 100px;gap:22px 10px">
    <div class="it"><span class="ic"></span><div><div class="h">Your Title</div><div class="p">Short detail.</div></div></div>
    <div class="it"><span class="ic b"></span><div><div class="h">Your Title</div><div class="p">Short detail.</div></div></div>
    <div class="it"><span class="ic b"></span><div><div class="h">Your Title</div><div class="p">Short detail.</div></div></div>
    <div class="it"><span class="ic"></span><div><div class="h">Your Title</div><div class="p">Short detail.</div></div></div>
  </div>
  <div class="abs" style="left:230px;top:50px;width:150px"><div class="h">Heading Goes Here</div><div class="p">Add a paragraph that ties the four points together in plain words.</div><div class="p" style="margin-top:5px">Follow with a short example for the group.</div></div>
  <div class="ft">Quill Harbor Labs</div>
</section>

<section class="slide">
  <div class="ttl"><b>Pictures</b> with Bullets</div><div class="brand"><i></i>QUILL HARBOR LABS</div>
  <div class="ph" role="img" aria-label="Photo of a speaker at a workshop" style="left:12px;top:42px;width:118px;height:70px"></div>
  <div class="ph warm" role="img" aria-label="Photo of learners at laptops" style="left:137px;top:42px;width:118px;height:70px"></div>
  <div class="ph" role="img" aria-label="Photo of a group discussion" style="left:262px;top:42px;width:118px;height:70px"></div>
  <div class="abs" style="left:12px;top:120px;width:118px"><div class="h">Heading Goes Here</div><div class="p">Short detail for this picture.</div></div>
  <div class="abs" style="left:137px;top:120px;width:118px"><div class="h">Heading Goes Here</div><div class="p">Short detail for this picture.</div></div>
  <div class="abs" style="left:262px;top:120px;width:118px"><div class="h">Heading Goes Here</div><div class="p">Short detail for this picture.</div></div>
  <div class="ft">Quill Harbor Labs</div>
</section>

<section class="slide">
  <div class="ttl"><b>Text</b> &amp; Bullet Area</div><div class="brand"><i></i>QUILL HARBOR LABS</div>
  <div class="abs" style="left:12px;top:44px;width:110px"><div class="h">Heading Goes Here</div><div class="p">Add a short paragraph about this set of points.</div><div class="p" style="margin-top:5px">Keep it simple.</div></div>
  <div class="abs" style="left:140px;top:48px;display:grid;grid-template-columns:118px 118px;gap:16px 6px">
    <div class="it"><span class="ic"></span><div><div class="h">Your Text Here</div><div class="p">Brief detail.</div></div></div>
    <div class="it"><span class="ic b"></span><div><div class="h">Your Text Here</div><div class="p">Brief detail.</div></div></div>
    <div class="it"><span class="ic b"></span><div><div class="h">Your Text Here</div><div class="p">Brief detail.</div></div></div>
    <div class="it"><span class="ic"></span><div><div class="h">Your Text Here</div><div class="p">Brief detail.</div></div></div>
    <div class="it"><span class="ic"></span><div><div class="h">Your Text Here</div><div class="p">Brief detail.</div></div></div>
    <div class="it"><span class="ic b"></span><div><div class="h">Your Text Here</div><div class="p">Brief detail.</div></div></div>
  </div>
  <div class="ft">Quill Harbor Labs</div>
</section>

<section class="slide">
  <div class="ttl"><b>Paragraph</b> with Three Bullet</div><div class="brand"><i></i>QUILL HARBOR LABS</div>
  <div class="abs" style="left:12px;top:44px;width:110px">
    <div class="lead">We are <em>Quill Harbor Labs</em><br>Be an Expert with Us</div>
    <div class="p" style="margin-top:6px">Add a short paragraph that sets up the three points on the right.</div>
  </div>
  <div class="abs c" style="left:140px;top:50px;width:75px"><span class="ic" style="display:inline-block;width:16px;height:16px"></span><div class="h">Your Title</div><div class="p">Short detail for this point.</div></div>
  <div class="abs c" style="left:222px;top:50px;width:75px"><span class="ic b" style="display:inline-block;width:16px;height:16px"></span><div class="h">Your Title</div><div class="p">Short detail for this point.</div></div>
  <div class="abs c" style="left:304px;top:50px;width:75px"><span class="ic" style="display:inline-block;width:16px;height:16px"></span><div class="h">Your Title</div><div class="p">Short detail for this point.</div></div>
  <div class="ft">Quill Harbor Labs</div>
</section>

<section class="slide">
  <div class="abs red-bg" style="left:0;top:0;width:170px;height:100px"></div>
  <div class="abs c" style="left:0;top:36px;width:170px;font-size:10px;font-weight:700;color:#fff;white-space:nowrap">QUILL HARBOR LABS</div>
  <div class="ph light" role="img" aria-label="Photo of a man working at a laptop" style="left:0;top:100px;width:170px;height:106px"></div>
  <div class="brand"><i></i>QUILL HARBOR LABS</div>
  <div class="abs" style="left:184px;top:34px;font-size:12px">Your Title Goes Here</div>
  <div class="abs" style="left:184px;top:54px;width:190px"><div class="p">Add a short paragraph that introduces these four points.</div></div>
  <div class="abs" style="left:184px;top:90px;display:grid;grid-template-columns:95px 95px;gap:14px 6px">
    <div class="it"><span class="ic"></span><div><div class="h">Your Text</div><div class="p">Brief detail.</div></div></div>
    <div class="it"><span class="ic"></span><div><div class="h">Your Text</div><div class="p">Brief detail.</div></div></div>
    <div class="it"><span class="ic"></span><div><div class="h">Your Text</div><div class="p">Brief detail.</div></div></div>
    <div class="it"><span class="ic"></span><div><div class="h">Your Text</div><div class="p">Brief detail.</div></div></div>
  </div>
  <div class="ft">Quill Harbor Labs</div>
</section>

<section class="slide">
  <div class="ttl"><b>Multiple</b> Column Area</div><div class="brand"><i></i>QUILL HARBOR LABS</div>
  <div class="abs" style="left:12px;top:44px;width:370px;display:grid;grid-template-columns:repeat(4,1fr);gap:6px">
    <div class="c"><span class="ic b" style="display:inline-block"></span><div class="p">Short note here</div></div>
    <div class="c"><span class="ic b" style="display:inline-block"></span><div class="p">Short note here</div></div>
    <div class="c"><span class="ic b" style="display:inline-block"></span><div class="p">Short note here</div></div>
    <div class="c"><span class="ic b" style="display:inline-block"></span><div class="p">Short note here</div></div>
  </div>
  <div class="abs" style="left:12px;top:90px;width:370px;height:1px;background:var(--line)"></div>
  <div class="abs" style="left:12px;top:104px;width:175px"><div class="h">Heading Goes Here</div><div class="p">Add a short paragraph with the first part of the idea.</div></div>
  <div class="abs" style="left:206px;top:104px;width:175px"><div class="h">Heading Goes Here</div><div class="p">Add a short paragraph with the second part of the idea.</div></div>
  <div class="ft">Quill Harbor Labs</div>
</section>

<section class="slide">
  <div class="ttl"><b>Your</b> Title Goes Here</div><div class="brand"><i></i>QUILL HARBOR LABS</div>
  <div class="abs" style="left:12px;top:36px;width:150px"><div class="h">Heading Goes Here</div><div class="p">Add a short intro line for this slide.</div></div>
  <div class="ph warm" role="img" aria-label="Photo of a team working on laptops" style="left:12px;top:62px;width:150px;height:130px"></div>
  <div class="ph" role="img" aria-label="Photo of colleagues reviewing code" style="left:166px;top:36px;width:105px;height:78px"></div>
  <div class="ph" role="img" aria-label="Photo of a woman smiling at a desk" style="left:275px;top:36px;width:105px;height:78px"></div>
  <div class="ph warm" role="img" aria-label="Photo of a workshop group" style="left:166px;top:118px;width:214px;height:74px"></div>
  <div class="ft">Quill Harbor Labs</div>
</section>

<section class="slide">
  <div class="ttl"><b>Global</b> Experience</div><div class="brand"><i></i>QUILL HARBOR LABS</div>
  <div class="ph light" role="img" aria-label="World map with red location markers" style="left:60px;top:36px;width:300px;height:130px"></div>
  <div class="abs it" style="left:12px;top:172px"><span class="ic"></span><div><div class="h">Heading Goes Here</div><div class="p">Short detail about reach.</div></div></div>
  <div class="ft">Quill Harbor Labs</div>
</section>

<section class="slide">
  <div class="brand"><i></i>QUILL HARBOR LABS</div>
  <div class="abs" style="left:12px;top:40px;font-size:13px;line-height:1.2">Video Title<br>Goes Here</div>
  <div class="abs" style="left:12px;top:82px;width:110px"><div class="p">Add a short note about the video and what learners should watch for.</div></div>
  <div class="ph light" role="img" aria-label="Desktop monitor showing a video on a desk" style="left:140px;top:30px;width:240px;height:160px"></div>
  <div class="abs circ" style="left:246px;top:90px;width:28px;height:20px;border-radius:5px;background:var(--red)">
    <svg width="10" height="10" viewBox="0 0 10 10"><polygon points="2,1 9,5 2,9" fill="#fff"/></svg>
  </div>
  <div class="ft">Quill Harbor Labs</div>
</section>

<section class="slide">
  <div class="ttl"><b>Four</b> Column Area</div><div class="brand"><i></i>QUILL HARBOR LABS</div>
  <div class="abs" style="left:12px;top:36px;width:370px"><div class="p">Add a short intro that explains the four columns below.</div></div>
  <div class="abs" style="left:12px;top:66px;width:370px;display:grid;grid-template-columns:repeat(4,1fr);gap:6px">
    <div class="red-bg c" style="height:100px;padding-top:14px"><span class="ic wh" style="display:inline-block;width:16px;height:16px"></span><div class="h w" style="margin-top:6px">Your Title</div><div class="p w" style="padding:0 6px">Short detail here.</div></div>
    <div class="blue-bg c" style="height:100px;padding-top:14px"><span class="ic wh" style="display:inline-block;width:16px;height:16px"></span><div class="h w" style="margin-top:6px">Your Title</div><div class="p w" style="padding:0 6px">Short detail here.</div></div>
    <div class="red-bg c" style="height:100px;padding-top:14px"><span class="ic wh" style="display:inline-block;width:16px;height:16px"></span><div class="h w" style="margin-top:6px">Your Title</div><div class="p w" style="padding:0 6px">Short detail here.</div></div>
    <div class="blue-bg c" style="height:100px;padding-top:14px"><span class="ic wh" style="display:inline-block;width:16px;height:16px"></span><div class="h w" style="margin-top:6px">Your Title</div><div class="p w" style="padding:0 6px">Short detail here.</div></div>
  </div>
  <div class="ft">Quill Harbor Labs</div>
</section>

<section class="slide">
  <div class="ttl"><b>Four</b> Column Area</div><div class="brand"><i></i>QUILL HARBOR LABS</div>
  <div class="abs c" style="left:40px;right:40px;top:36px"><div class="p">Add a short intro that explains the four columns below.</div></div>
  <div class="abs" style="left:12px;top:62px;width:370px;display:grid;grid-template-columns:repeat(4,1fr);gap:6px">
    <div class="c"><div class="circ" style="margin:0 auto;width:40px;height:40px;border:3px solid var(--red)"><span class="ic"></span></div><div class="h" style="margin-top:6px">Column 1</div><div class="p">Short detail.</div></div>
    <div class="c"><div class="circ" style="margin:0 auto;width:40px;height:40px;border:3px solid var(--blue)"><span class="ic b"></span></div><div class="h" style="margin-top:6px">Column 2</div><div class="p">Short detail.</div></div>
    <div class="c"><div class="circ" style="margin:0 auto;width:40px;height:40px;border:3px solid var(--red)"><span class="ic"></span></div><div class="h" style="margin-top:6px">Column 3</div><div class="p">Short detail.</div></div>
    <div class="c"><div class="circ" style="margin:0 auto;width:40px;height:40px;border:3px solid var(--blue)"><span class="ic b"></span></div><div class="h" style="margin-top:6px">Column 4</div><div class="p">Short detail.</div></div>
  </div>
  <div class="ft">Quill Harbor Labs</div>
</section>

<section class="slide">
  <div class="ttl"><b>Key</b> Points Area</div><div class="brand"><i></i>QUILL HARBOR LABS</div>
  <div class="abs" style="left:12px;top:36px;width:370px"><div class="p">Add a short intro that explains the key points shown below.</div></div>
  <div class="abs" style="left:60px;top:62px;width:270px;height:46px;border-radius:23px;background:var(--soft);display:flex;justify-content:space-around;align-items:center">
    <span class="circ" style="width:30px;height:30px;background:var(--red)"></span>
    <span class="circ" style="width:30px;height:30px;background:var(--blue)"></span>
    <span class="circ" style="width:30px;height:30px;background:var(--red)"></span>
    <span class="circ" style="width:30px;height:30px;background:var(--blue)"></span>
    <span class="circ" style="width:30px;height:30px;background:var(--red)"></span>
  </div>
  <div class="abs" style="left:12px;top:128px;width:175px"><div class="p">Add a short paragraph that explains the first half of the points.</div></div>
  <div class="abs" style="left:206px;top:128px;width:175px"><div class="p">Add a short paragraph that explains the second half of the points.</div></div>
  <div class="ft">Quill Harbor Labs</div>
</section>

<section class="slide">
  <div class="ttl"><b>Process</b> Area</div><div class="brand"><i></i>QUILL HARBOR LABS</div>
  <svg class="abs" style="left:0;top:0" width="393" height="206">
    <rect x="20" y="50" width="354" height="120" fill="#f1f1f1"/>
    <g fill="none" stroke="#999" stroke-width=".8">
      <path d="M197 80 V100"/><path d="M197 130 V148"/>
      <path d="M80 115 H100"/><path d="M140 115 H160"/><path d="M234 115 H254"/><path d="M294 115 H314"/>
    </g>
    <g fill="#fff" stroke="#bbb" stroke-width=".6">
      <rect x="172" y="62" width="50" height="18"/><rect x="160" y="100" width="74" height="30"/><rect x="172" y="148" width="50" height="16"/>
    </g>
    <g fill="var(--red)"><circle cx="70" cy="115" r="8"/><circle cx="130" cy="115" r="8"/><circle cx="264" cy="115" r="8"/><circle cx="324" cy="115" r="8"/></g>
    <g font-size="4.5" fill="#555" font-family="Open Sans, sans-serif" text-anchor="middle">
      <text x="197" y="73">Process 01</text><text x="197" y="117">Main Step</text><text x="197" y="158">Process 02</text>
    </g>
  </svg>
  <div class="abs" style="left:30px;top:60px;width:90px"><div class="h">Process Here</div><div class="p">Short detail.</div></div>
  <div class="ft">Quill Harbor Labs</div>
</section>

<section class="slide">
  <div class="ttl"><b>Workflow</b> Area</div><div class="brand"><i></i>QUILL HARBOR LABS</div>
  <div class="abs c" style="left:40px;right:40px;top:36px"><div class="p">Add a short intro that explains the workflow shown below.</div></div>
  <svg class="abs" style="left:0;top:60px" width="393" height="110">
    <path d="M30 55 Q 80 5 130 55 T 230 55 T 330 55" fill="none" stroke="var(--red)" stroke-width="9"/>
    <path d="M80 55 Q 130 105 180 55 T 280 55 T 370 55" fill="none" stroke="var(--blue)" stroke-width="9" opacity=".9"/>
    <g fill="#fff" stroke="#ddd"><circle cx="80" cy="30" r="10"/><circle cx="180" cy="80" r="10"/><circle cx="230" cy="30" r="10"/><circle cx="330" cy="80" r="10"/></g>
    <g font-size="5" font-weight="700" fill="#333" font-family="Open Sans, sans-serif" text-anchor="middle">
      <text x="80" y="32">01</text><text x="180" y="82">02</text><text x="230" y="32">03</text><text x="330" y="82">04</text>
    </g>
  </svg>
  <div class="abs" style="left:60px;top:174px;width:90px"><div class="h">Your Title</div><div class="p">Short detail.</div></div>
  <div class="abs" style="left:240px;top:174px;width:90px"><div class="h">Your Title</div><div class="p">Short detail.</div></div>
  <div class="ft">Quill Harbor Labs</div>
</section>

<section class="slide">
  <div class="ttl"><b>Timeline</b></div><div class="brand"><i></i>QUILL HARBOR LABS</div>
  <svg class="abs" style="left:0;top:0" width="393" height="206">
    <path d="M40 110 L110 80 L190 110 L270 80 L350 110" fill="none" stroke="#ccc" stroke-width="1"/>
    <g><circle cx="40" cy="110" r="18" fill="var(--red)"/><circle cx="110" cy="80" r="14" fill="var(--blue)"/><circle cx="190" cy="110" r="18" fill="var(--red)"/><circle cx="270" cy="80" r="14" fill="var(--blue)"/><circle cx="350" cy="110" r="18" fill="var(--red)"/></g>
    <g font-size="6" font-weight="700" fill="#fff" font-family="Open Sans, sans-serif" text-anchor="middle">
      <text x="40" y="112">2013</text><text x="110" y="82">2014</text><text x="190" y="112">2015</text><text x="270" y="82">2016</text><text x="350" y="112">2017</text>
    </g>
  </svg>
  <div class="abs" style="left:20px;top:140px;width:100px"><div class="h">Your Text Here</div><div class="p">Short milestone note.</div></div>
  <div class="abs" style="left:150px;top:140px;width:100px"><div class="h">Your Text Here</div><div class="p">Short milestone note.</div></div>
  <div class="abs" style="left:290px;top:140px;width:90px"><div class="h">Your Text Here</div><div class="p">Short milestone note.</div></div>
  <div class="ft">Quill Harbor Labs</div>
</section>

<section class="slide">
  <div class="ttl"><b>Bullet</b> &amp; Chart Area</div><div class="brand"><i></i>QUILL HARBOR LABS</div>
  <div class="abs col" style="left:40px;top:50px;gap:14px;width:150px">
    <div style="display:flex;flex-direction:column;gap:2px"><div style="height:5px;width:120px;background:var(--red)"></div><div style="height:5px;width:90px;background:var(--blue)"></div></div>
    <div style="display:flex;flex-direction:column;gap:2px"><div style="height:5px;width:80px;background:var(--red)"></div><div style="height:5px;width:130px;background:var(--blue)"></div></div>
    <div style="display:flex;flex-direction:column;gap:2px"><div style="height:5px;width:140px;background:var(--red)"></div><div style="height:5px;width:70px;background:var(--blue)"></div></div>
    <div style="display:flex;flex-direction:column;gap:2px"><div style="height:5px;width:100px;background:var(--red)"></div><div style="height:5px;width:110px;background:var(--blue)"></div></div>
  </div>
  <div class="abs" style="left:38px;top:46px;width:1px;height:110px;background:#bbb"></div>
  <div class="abs col" style="left:220px;top:46px;gap:10px;width:160px">
    <div class="it"><span class="ic"></span><div><div class="h">Update Here</div><div class="p">Short detail.</div></div></div>
    <div class="it"><span class="ic b"></span><div><div class="h">Update Here</div><div class="p">Short detail.</div></div></div>
    <div class="it"><span class="ic"></span><div><div class="h">Update Here</div><div class="p">Short detail.</div></div></div>
    <div class="it"><span class="ic b"></span><div><div class="h">Update Here</div><div class="p">Short detail.</div></div></div>
  </div>
  <div class="ft">Quill Harbor Labs</div>
</section>

<section class="slide">
  <div class="ttl"><b>Table</b> Area</div><div class="brand"><i></i>QUILL HARBOR LABS</div>
  <div class="abs" style="left:40px;top:40px;width:310px;display:grid;grid-template-columns:1.4fr 1fr 1fr 1fr;font-size:4.5px;text-align:center">
    <div style="background:#444;color:#fff;padding:8px 4px;text-align:left;font-weight:700">Description</div>
    <div style="background:var(--red);color:#fff;padding:8px 4px;font-weight:700">Option 1</div>
    <div style="background:#555;color:#fff;padding:8px 4px;font-weight:700">Option 2</div>
    <div style="background:var(--blue);color:#fff;padding:8px 4px;font-weight:700">Option 3</div>
    <div style="padding:5px 4px;text-align:left;background:var(--soft)">Feature One</div><div style="padding:5px;background:var(--soft)">✓</div><div style="padding:5px;background:var(--soft)">✓</div><div style="padding:5px;background:var(--soft)">✓</div>
    <div style="padding:5px 4px;text-align:left">Feature Two</div><div style="padding:5px">✓</div><div style="padding:5px">–</div><div style="padding:5px">✓</div>
    <div style="padding:5px 4px;text-align:left;background:var(--soft)">Feature Three</div><div style="padding:5px;background:var(--soft)">✓</div><div style="padding:5px;background:var(--soft)">✓</div><div style="padding:5px;background:var(--soft)">–</div>
    <div style="padding:5px 4px;text-align:left">Feature Four</div><div style="padding:5px">–</div><div style="padding:5px">✓</div><div style="padding:5px">✓</div>
    <div style="padding:5px 4px;text-align:left;background:var(--soft)">Feature Five</div><div style="padding:5px;background:var(--soft)">✓</div><div style="padding:5px;background:var(--soft)">–</div><div style="padding:5px;background:var(--soft)">✓</div>
    <div style="padding:5px 4px;text-align:left">Feature Six</div><div style="padding:5px">✓</div><div style="padding:5px">✓</div><div style="padding:5px">✓</div>
  </div>
  <div class="ft">Quill Harbor Labs</div>
</section>

<section class="slide">
  <div class="ttl"><b>Bullet</b> &amp; Chart Area</div><div class="brand"><i></i>QUILL HARBOR LABS</div>
  <div class="abs col" style="left:12px;top:44px;gap:8px;width:180px">
    <div class="it"><span class="ic"></span><div><div class="h">Your Text Here</div><div class="p">Short detail.</div></div></div>
    <div class="it"><span class="ic b"></span><div><div class="h">Your Text Here</div><div class="p">Short detail.</div></div></div>
    <div class="it"><span class="ic"></span><div><div class="h">Your Text Here</div><div class="p">Short detail.</div></div></div>
    <div class="it"><span class="ic b"></span><div><div class="h">Your Text Here</div><div class="p">Short detail.</div></div></div>
  </div>
  <svg class="abs" style="left:230px;top:48px" width="140" height="120" viewBox="0 0 140 120">
    <circle cx="70" cy="60" r="36" fill="none" stroke="#ddd" stroke-width="14"/>
    <circle cx="70" cy="60" r="36" fill="none" stroke="var(--red)" stroke-width="14" stroke-dasharray="151 226" transform="rotate(-90 70 60)"/>
    <circle cx="70" cy="60" r="36" fill="none" stroke="var(--blue)" stroke-width="14" stroke-dasharray="34 226" stroke-dashoffset="-151" transform="rotate(-90 70 60)"/>
    <g font-family="Open Sans, sans-serif" font-weight="700" font-size="9">
      <text x="118" y="62" fill="var(--red)">67%</text><text x="2" y="40" fill="var(--red)">15%</text><text x="8" y="86" fill="var(--blue)">18%</text><text x="62" y="14" fill="#999">100%</text>
    </g>
  </svg>
  <div class="ft">Quill Harbor Labs</div>
</section>

<section class="slide">
  <div class="ttl"><b>Pricing</b> Structure</div><div class="brand"><i></i>QUILL HARBOR LABS</div>
  <div class="abs" style="left:12px;top:40px;width:370px;display:grid;grid-template-columns:1.6fr 1fr 1fr 1fr;gap:2px 6px;font-size:4.5px;text-align:center">
    <div class="h" style="text-align:left;font-size:7px">Choose Your Plan</div>
    <div style="background:var(--soft);padding:4px;font-weight:700">Basic</div><div style="background:var(--soft);padding:4px;font-weight:700">Standard</div><div style="background:var(--soft);padding:4px;font-weight:700">Premium</div>
    <div style="text-align:left;padding:4px 0">• Unlimited lab time</div><div>✓</div><div>✓</div><div>✓</div>
    <div style="text-align:left;padding:4px 0">• Course workbooks</div><div>✓</div><div>✕</div><div>✓</div>
    <div style="text-align:left;padding:4px 0">• Mentor sessions</div><div>✕</div><div>✓</div><div>✓</div>
    <div style="text-align:left;padding:4px 0">• Code reviews</div><div>✓</div><div>✓</div><div>✓</div>
    <div style="text-align:left;padding:4px 0">• Certificate</div><div>✕</div><div>✓</div><div>✓</div>
    <div style="text-align:left;padding:4px 0;font-weight:700">Total</div>
    <div style="background:#444;color:#fff;padding:4px">$99</div><div style="background:var(--blue);color:#fff;padding:4px">$199</div><div style="background:var(--red);color:#fff;padding:4px">$299</div>
  </div>
  <div class="ft">Quill Harbor Labs</div>
</section>

<section class="slide">
  <div class="ph" role="img" aria-label="Team photo area" style="left:0;top:0;width:130px;height:206px"></div>
  <div class="abs red-bg" style="left:0;top:150px;width:130px;height:30px;padding:8px 12px;font-size:9px;color:#fff">Meet Our Team</div>
  <div class="brand"><i></i>QUILL HARBOR LABS</div>
  <div class="abs" style="left:146px;top:24px;display:grid;grid-template-columns:120px 120px;gap:12px 6px">
    <div class="it"><span class="ph light" role="img" aria-label="Team member portrait" style="position:relative;width:28px;height:28px;border-radius:50%;border:2px solid var(--red);flex:none"></span><div><div class="h">Mara Lind</div><div class="p">Lead Trainer</div></div></div>
    <div class="it"><span class="ph light" role="img" aria-label="Team member portrait" style="position:relative;width:28px;height:28px;border-radius:50%;border:2px solid var(--red);flex:none"></span><div><div class="h">Oren Vale</div><div class="p">Course Author</div></div></div>
    <div class="it"><span class="ph light" role="img" aria-label="Team member portrait" style="position:relative;width:28px;height:28px;border-radius:50%;border:2px solid var(--red);flex:none"></span><div><div class="h">Ines Roark</div><div class="p">Lab Mentor</div></div></div>
    <div class="it"><span class="ph light" role="img" aria-label="Team member portrait" style="position:relative;width:28px;height:28px;border-radius:50%;border:2px solid var(--red);flex:none"></span><div><div class="h">Tomas Brandt</div><div class="p">Code Reviewer</div></div></div>
    <div class="it"><span class="ph light" role="img" aria-label="Team member portrait" style="position:relative;width:28px;height:28px;border-radius:50%;border:2px solid var(--red);flex:none"></span><div><div class="h">Lena Hoyt</div><div class="p">Support Lead</div></div></div>
    <div class="it"><span class="ph light" role="img" aria-label="Team member portrait" style="position:relative;width:28px;height:28px;border-radius:50%;border:2px solid var(--red);flex:none"></span><div><div class="h">Pavel Dorn</div><div class="p">Developer</div></div></div>
  </div>
  <div class="ft">Quill Harbor Labs</div>
</section>

<section class="slide">
  <div class="ph red" role="img" aria-label="Red toned photo of hands typing on a keyboard" style="left:0;top:0;width:100%;height:206px"></div>
  <div class="abs red-bg" style="left:0;top:0;width:150px;height:206px;padding:20px 14px">
    <div style="font-size:10px;font-weight:700;color:#fff;text-align:center;margin-bottom:16px;white-space:nowrap">QUILL HARBOR LABS</div>
    <div style="font-size:10px;color:#fff;margin-bottom:8px">Our Contact</div>
    <div class="col" style="gap:6px">
      <div class="it"><span class="ic wh" style="width:9px;height:9px"></span><div class="p w">+1 555 014 2290</div></div>
      <div class="it"><span class="ic wh" style="width:9px;height:9px"></span><div class="p w">hello@quillharborlabs.dev</div></div>
      <div class="it"><span class="ic wh" style="width:9px;height:9px"></span><div class="p w">www.quillharborlabs.dev</div></div>
      <div class="it"><span class="ic wh" style="width:9px;height:9px"></span><div class="p w">12 Harbor Lane, Suite 4</div></div>
    </div>
  </div>
  <div class="abs" style="left:230px;top:80px;font-size:16px;font-weight:700;color:#fff">THANK YOU</div>
  <div class="abs" style="left:230px;top:102px;width:140px"><div class="p w">Questions are welcome. See you in the next lab.</div></div>
  <div class="ft">Quill Harbor Labs</div>
</section>

</main>
</body>
</html>
```